Wireless Broadband Newspaper AD

We have recently re-branded our company, new logo and website.

Our primary product offering is Wireless Broadband services to region, the target audience generally cannot get ADSL broadband.

We wanted to pose the question "Can't get ADSL ?" to attract the attention of those who are unable to access conventional mass market broadband offerings.

Ad Size should be:
129mm Wide
178mm High

Please find the text for the AD below.

Can't get ADSL ?
Try Fixed Wireless Broadband

* Speeds up to 10Mbit
* Plans from $29.95 per month
* Up to 60GB Download Allowance
* $99 Professional On-site Installation
* No Contracts

http://pelnetlink.com.au
CALL NOW - 1300 47 91 63

-

Target Market(s)

Frequent Internet users, requiring broadband access in their homes.

Industry/Entity Type

It Company

Requirements
Must have
• Ensure that the general branding feel of the existing website is considered, please us similar colours and theme.
• As well as our logo, which you will find attached in EPS format.
• http://pelnetlink.com.au
Nice to have
• Large caption "Can't get ADSL?"

```html
<!DOCTYPE html>
<html lang="en">
<head>
<meta charset="utf-8">
<title>Pelnet Link – Fixed Wireless Broadband Ad</title>
<link href="https://fonts.googleapis.com/css2?family=Roboto+Condensed:wght@700&family=Arimo:wght@400;700&display=swap" rel="stylesheet">
<style>
  :root {
    --paper: #ffffff;
    --red: #e8200c;
    --red-deep: #b80d05;
    --orange: #f7941d;
    --amber: #ffb400;
    --dark: #2a0a04;
    --ink: #111111;
    --grey-line: #9a9a9a;
    --grey-light: #f2f2f2;
    --grey-mid: #d9d9d9;
    --mark: #8a8a8a;
  }
  * { box-sizing: border-box; margin: 0; padding: 0; }
  html, body { width: 1200px; height: 1200px; overflow: hidden; background: var(--paper); }
  .sheet { position: relative; width: 1200px; height: 1200px; }

  .crop { position: absolute; background: var(--mark); }
  .crop.v { width: 1px; height: 40px; }
  .crop.h { width: 52px; height: 1px; }

  .ad {
    position: absolute; left: 236px; top: 94px; width: 728px; height: 1010px;
    background: var(--paper); overflow: hidden;
    font-family: "Arimo", Arial, sans-serif;
  }

  .header { position: absolute; left: 0; top: 0; width: 728px; height: 250px;
    background: linear-gradient(180deg, var(--orange), var(--amber)); }
  .header-panel { position: absolute; left: 30px; top: 26px; right: 0; bottom: 0;
    border-top-left-radius: 26px;
    background: linear-gradient(180deg, #f5430f 0%, var(--red) 45%, var(--red-deep) 100%); }
  .headline { position: absolute; left: 0; right: 0; top: 84px; text-align: center;
    font-family: "Roboto Condensed", "Arial Narrow", sans-serif; font-weight: 700;
    font-size: 100px; line-height: 1; color: #fff; letter-spacing: -2px;
    text-shadow: 0 3px 4px rgba(80,0,0,.45); }

  .subline { position: absolute; left: 0; top: 250px; width: 728px; height: 86px;
    background: linear-gradient(180deg, var(--dark) 0%, #6a1405 40%, var(--red) 75%, var(--amber) 100%);
    display: flex; align-items: center; justify-content: center; padding-bottom: 4px;
    font-family: "Roboto Condensed", "Arial Narrow", sans-serif; font-weight: 700;
    font-size: 44px; color: #fff; }

  .features { position: absolute; left: 60px; top: 370px; list-style: none; }
  .features li { display: flex; align-items: center; height: 40px;
    font-size: 34px; color: var(--ink); letter-spacing: -0.3px; }
  .features svg { width: 28px; height: 28px; margin-right: 12px; flex: none; }

  .call-badge { position: absolute; left: 204px; top: 604px; width: 320px; height: 84px; }
  .call-text { position: absolute; left: 204px; top: 604px; width: 320px; height: 84px;
    display: flex; align-items: center; justify-content: center;
    font-family: "Roboto Condensed", "Arial Narrow", sans-serif; font-weight: 700;
    font-size: 44px; color: #fff; text-shadow: 0 2px 3px rgba(60,0,0,.6); }

  .phone { position: absolute; left: 0; right: 0; top: 698px; text-align: center;
    font-family: "Arimo", Arial, sans-serif; font-weight: 700; font-size: 92px;
    line-height: 1; letter-spacing: -1px;
    background: linear-gradient(180deg, var(--amber) 0%, var(--red) 45%, var(--red-deep) 100%);
    -webkit-background-clip: text; background-clip: text; color: transparent; }

  .rule { position: absolute; left: 0; top: 798px; width: 728px; height: 5px; background: var(--grey-line); }
  .brand-band { position: absolute; left: 0; top: 803px; width: 728px; height: 143px;
    background: linear-gradient(180deg, var(--grey-light), var(--grey-mid));
    display: flex; align-items: center; justify-content: center; gap: 16px; }
  .brand-dot { width: 52px; height: 52px; border-radius: 50%; background: var(--red); }
  .brand-name { font-family: "Arimo", Arial, sans-serif; font-weight: 700; font-size: 56px;
    color: #333; letter-spacing: -1px; }

  .footer { position: absolute; left: 0; top: 946px; width: 728px; height: 64px;
    background: linear-gradient(180deg, var(--red-deep), var(--red) 50%, var(--orange));
    display: flex; align-items: center; justify-content: center;
    font-size: 32px; color: #fff; }
</style>
</head>
<body>
<div class="sheet">
  <span class="crop v" style="left:236px;top:28px"></span>
  <span class="crop v" style="left:964px;top:28px"></span>
  <span class="crop h" style="left:160px;top:94px"></span>
  <span class="crop h" style="left:988px;top:94px"></span>
  <span class="crop v" style="left:236px;top:1128px"></span>
  <span class="crop v" style="left:964px;top:1128px"></span>
  <span class="crop h" style="left:160px;top:1104px"></span>
  <span class="crop h" style="left:988px;top:1104px"></span>

  <div class="ad">
    <div class="header">
      <div class="header-panel"></div>
      <h1 class="headline">Can’t get ADSL?</h1>
    </div>
    <div class="subline">Try Fixed Wireless Broadband !</div>

    <ul class="features">
      <li><svg viewBox="0 0 28 28"><rect x="2" y="6" width="20" height="20" fill="#fff" stroke="#111" stroke-width="2.5"/><path d="M6 15l5 6L26 2" fill="none" stroke="#e8200c" stroke-width="3"/></svg>Speeds up to 10Mbit</li>
      <li><svg viewBox="0 0 28 28"><rect x="2" y="6" width="20" height="20" fill="#fff" stroke="#111" stroke-width="2.5"/><path d="M6 15l5 6L26 2" fill="none" stroke="#e8200c" stroke-width="3"/></svg>Plans from $29.95 per month</li>
      <li><svg viewBox="0 0 28 28"><rect x="2" y="6" width="20" height="20" fill="#fff" stroke="#111" stroke-width="2.5"/><path d="M6 15l5 6L26 2" fill="none" stroke="#e8200c" stroke-width="3"/></svg>Up to 60GB Download Allowance</li>
      <li><svg viewBox="0 0 28 28"><rect x="2" y="6" width="20" height="20" fill="#fff" stroke="#111" stroke-width="2.5"/><path d="M6 15l5 6L26 2" fill="none" stroke="#e8200c" stroke-width="3"/></svg>$99 Professional On-site Installation</li>
      <li><svg viewBox="0 0 28 28"><rect x="2" y="6" width="20" height="20" fill="#fff" stroke="#111" stroke-width="2.5"/><path d="M6 15l5 6L26 2" fill="none" stroke="#e8200c" stroke-width="3"/></svg>No Contracts</li>
    </ul>

    <svg class="call-badge" viewBox="0 0 320 80" preserveAspectRatio="none" aria-hidden="true">
      <defs>
        <radialGradient id="burst-fill" cx="50%" cy="50%" r="50%">
          <stop offset="0%" stop-color="#f7941d"/>
          <stop offset="70%" stop-color="#e8200c"/>
          <stop offset="100%" stop-color="#9c0a03"/>
        </radialGradient>
      </defs>
      <polygon fill="url(#burst-fill)" points="320,40 280.8,47.3 298.6,60 248.4,59.8 240,74.6 192.4,67 160,80 127.6,67 80,74.6 71.6,59.8 21.4,60 39.2,47.3 0,40 39.2,32.7 21.4,20 71.6,20.2 80,5.4 127.6,13 160,0 192.4,13 240,5.4 248.4,20.2 298.6,20 280.8,32.7"/>
      <ellipse cx="160" cy="40" rx="118" ry="26" fill="url(#burst-fill)"/>
    </svg>
    <div class="call-text">Call Now</div>

    <div class="phone">1300 47 91 63</div>

    <div class="rule"></div>
    <div class="brand-band">
      <span class="brand-dot"></span>
      <span class="brand-name">pelnet link</span>
    </div>

    <div class="footer">http://pelnetlink.com.au</div>
  </div>
</div>
</body>
</html>
```